依頼詳細
弊社得意先へ出す年賀状のデザインをお願いいたします。
・裏面のみ(片面)
・通常のはがきサイズ
・弊社ロゴ、WEBサイトのトン&マナからあまりずれない範囲の色・デザイン
(弊社コーポレート:https://sorane-link.jp/
記載項目
【裏面】
①会社名:株式会社ハルモアネットワークス
②代表名:代表取締役社長 浜田 諒
③住所:〒105-0048 東京都港区芝浜4-27-8 KNビル3F
④電話:代表番号 03-5872-3157
⑥本文:以下
謹んで新春のお慶びを申し上げます
(or 謹賀新年)

旧年中は格別のお引き立てを賜り厚く御礼申し上げます
皆様のご健勝とご多幸を心よりお祈りいたしますとともに
本年も何卒ご愛顧のほどよろしくお願い申し上げます

令和五年元日
希望イメージ
シンプル 複雑
単色 カラフル
暗い 明るい
日常 高級
遊び心 厳粛
未来的 伝統的
女性的 男性的
希望する色
赤系、無彩色系
納品ファイル
• イラストレーター形式 (.ai)
■ 選んだ理由

対法人に対する年賀状は皆様もご存じの通り、一般的なデザインのものは目に留まりにくいものでございます。(多くの年賀状に埋もれてしまう)
その中で、今回当選とさせていただいたデザインは、弊社からの年賀状ということが一目瞭然であり、あまり類を見ないデザインでございましたので、選ばせていただきました。

■ 提案者全員のお礼・コメント

今回、初めてBrimlyというサービスを活用させていただきました。
使い勝手も分からず、提案内容においてもご提案しにくい文面になっていたことと思います。
そんな中、多くのご提案をいただけたこと、また皆様の丁寧なご対応に驚きを隠せません。

今後は、弊社の事業の中でも皆様のお力添えをいただきたく、必要に応じて利用させていただければと考えております。

年末近く、皆様ご多用の中、多くの素晴らしいご提案を下さったこと、改めてお礼申し上げます。
今後ともどうぞよろしくお願いいたします。

```html
<!DOCTYPE html>
<html lang="ja">
<head>
<meta charset="utf-8">
<title>年賀状 令和五年</title>
<link rel="stylesheet" href="https://fonts.googleapis.com/css2?family=Noto+Serif+JP:wght@400;600;700;900&family=Noto+Sans+JP:wght@400;500&display=swap">
<style>
  :root {
    --red: #d0121b;
    --gold: #c9a54a;
    --ink: #1e1e1e;
    --gray: #6a6a6a;
    --paper: #ffffff;
  }
  * { margin: 0; padding: 0; box-sizing: border-box; }
  html, body { width: 809px; height: 1200px; overflow: hidden; background: var(--paper); }
  .card {
    position: relative;
    width: 809px;
    height: 1200px;
    background: var(--paper);
    font-family: "Noto Serif JP", serif;
    color: var(--ink);
    overflow: hidden;
  }
  .shapes { position: absolute; inset: 0; }
  .vertical {
    position: absolute;
    writing-mode: vertical-rl;
    white-space: nowrap;
  }
  .zodiac {
    position: absolute;
    left: 0; top: 0;
    width: 256px; height: 310px;
    display: flex; align-items: center; justify-content: center;
    font-size: 178px; font-weight: 900; color: var(--gold);
    line-height: 1;
  }
  .greeting {
    left: 668px; top: 40px;
    font-size: 72px; font-weight: 600;
    color: var(--gold);
    letter-spacing: 0.04em;
  }
  .message {
    font-size: 23px; font-weight: 600;
    letter-spacing: 0.08em;
    top: 82px;
  }
  .message--1 { left: 592px; }
  .message--2 { left: 526px; }
  .message--3 { left: 460px; }
  .date {
    left: 394px; top: 430px;
    font-size: 21px; font-weight: 600;
    letter-spacing: 0.12em;
  }
  .brand {
    position: absolute;
    left: 62px; top: 560px;
    display: flex; align-items: center; gap: 10px;
    font-family: "Noto Sans JP", sans-serif;
    font-size: 34px; font-weight: 400;
    color: var(--gray);
    letter-spacing: 0.02em;
  }
  .brand__mark { width: 14px; height: 14px; background: var(--red); }
  .contact {
    font-family: "Noto Sans JP", sans-serif;
    font-size: 13px; font-weight: 400;
    color: var(--gray);
    top: 650px;
    letter-spacing: 0.05em;
  }
  .contact--zip { left: 250px; }
  .contact--address { left: 232px; }
  .contact--phone { left: 214px; }
  .company {
    left: 168px; top: 650px;
    font-size: 25px; font-weight: 700;
    letter-spacing: 0.06em;
  }
  .rep-title {
    left: 116px; top: 1000px;
    font-family: "Noto Sans JP", sans-serif;
    font-size: 12px; color: var(--gray);
    letter-spacing: 0.08em;
  }
  .rep-name {
    left: 56px; top: 1000px;
    font-size: 34px; font-weight: 700;
    letter-spacing: 0.1em;
  }
  .year {
    left: 598px; top: 880px;
    font-size: 40px; font-weight: 600;
    color: var(--red);
    letter-spacing: 0.02em;
  }
</style>
</head>
<body>
<main class="card">
  <svg class="shapes" width="809" height="1200" viewBox="0 0 809 1200" aria-hidden="true">
    <!-- zodiac badge -->
    <polygon points="128,13 251,84 251,226 128,297 5,226 5,84" fill="var(--red)"/>
    <!-- year cluster -->
    <polygon points="729,665 824,720 824,830 729,885 634,830 634,720" fill="var(--red)"/>
    <polygon points="540,775 579,797 579,843 540,865 501,843 501,797" fill="var(--red)"/>
    <polygon points="620,805 715,860 715,1060 620,1115 525,1060 525,860" fill="var(--paper)" stroke="var(--red)" stroke-width="3"/>
    <polygon points="745,1010 840,1065 840,1175 745,1230 650,1175 650,1065" fill="var(--gold)"/>
  </svg>

  <div class="zodiac">卯</div>

  <h1 class="vertical greeting">謹賀新年</h1>

  <p class="vertical message message--1">旧年中は格別のお引き立てを賜り厚く御礼申し上げます</p>
  <p class="vertical message message--2">皆様のご健勝とご多幸を心よりお祈りいたしますとともに</p>
  <p class="vertical message message--3">本年も何卒ご愛顧のほどよろしくお願い申し上げます</p>
  <p class="vertical date">令和五年　元日</p>

  <div class="brand"><span class="brand__mark"></span><span>sorane</span></div>

  <p class="vertical contact contact--zip">〒105-0048</p>
  <p class="vertical contact contact--address">東京都港区芝浜4-27-8 KNビル3F</p>
  <p class="vertical contact contact--phone">代表番号　03-5872-3157</p>
  <p class="vertical company">株式会社ハルモアネットワークス</p>
  <p class="vertical rep-title">代表取締役社長</p>
  <p class="vertical rep-name">浜田　諒</p>

  <p class="vertical year">二〇二三</p>
</main>
</body>
</html>
```